realtor require a flyer to market a unit in prime district singapore

This flyer for the sale of "The Vallombre" is to be distributed to high class district in PRIME homes in singapore. It has to be elegant but eye catching. It must also contain the following detail

1) 1605sqft
2) $2.4 mil with room for negotiation
3) Owner migrating
4) 3 + utility room
5) Marcus Tierney
6) 83527406
7) CEA no. 4172539K

In Singapore the marketing law is pretty strict hence, the following information must also be shown but may be in fine line

1) OKA Homefield network Pte Ltd with LOGO
2) Estate Agency License L7185640M

Target Market(s)

High network owners who has only that 1 sec to to catch their attention

Industry/Entity Type

Marketing

Font styles to use
Serif

Requirements
Must have
• What is stated above
Nice to have
• Nice to have the works and layout nicely crafted out

```html
<!DOCTYPE html>
<html lang="en">
<head>
<meta charset="utf-8">
<title>The Vallombre – Property Flyer</title>
<link rel="stylesheet" href="https://fonts.googleapis.com/css2?family=Open+Sans:ital,wght@0,400;0,700;0,800;1,400;1,700;1,800&family=Oswald:wght@500;600;700&family=Tinos:wght@400;700&display=swap">
<style>
  :root {
    --red: #d8121f;
    --navy: #1b2391;
    --blue: #2a35c4;
    --white: #ffffff;
    --silver: #c9c9cc;
    --page: #f2f2f2;
  }
  * { box-sizing: border-box; margin: 0; padding: 0; }
  html, body { width: 889px; height: 1200px; overflow: hidden; background: var(--page); }
  .flyer { position: relative; width: 889px; height: 1200px; overflow: hidden; background: var(--white); font-family: "Open Sans", Arial, sans-serif; }

  .hero-photo {
    position: absolute; left: 0; top: 200px; width: 889px; height: 470px;
    background: linear-gradient(100deg, #6b4328 0%, #8a5a36 12%, #e6dccb 22%, #efe8da 55%, #d9cdb8 75%, #4a4040 100%);
  }
  .backdrop { position: absolute; inset: 0; }

  .brand { position: absolute; left: 50px; top: 118px; display: flex; align-items: center; gap: 10px; }
  .brand-square { width: 34px; height: 34px; background: var(--red); }
  .brand-name { font-family: "Tinos", "Times New Roman", serif; font-weight: 700; font-size: 30px; color: var(--navy); }

  .headline { position: absolute; right: 28px; top: 62px; text-align: right; }
  .headline-lead { font-weight: 800; font-style: italic; font-size: 37px; color: var(--red); letter-spacing: -0.5px; line-height: 1.05; }
  .headline-main { font-weight: 800; font-style: italic; font-size: 60px; color: var(--red); letter-spacing: -1px; line-height: 1.05; }
  .headline-tag { font-family: "Tinos", "Times New Roman", serif; font-size: 19px; color: var(--navy); margin-top: 6px; }

  .thumb {
    position: absolute; border: 6px solid var(--white); border-radius: 20px;
    box-shadow: 0 3px 8px rgba(0,0,0,0.45);
  }
  .thumb-living { left: 46px; top: 532px; width: 262px; height: 174px; background: linear-gradient(160deg, #f2efe8, #cfc6b6 55%, #5b3a2a); }
  .thumb-patio { left: 97px; top: 734px; width: 259px; height: 173px; background: linear-gradient(160deg, #6f8f4c, #c8c7bd 50%, #3e4a2f); }
  .thumb-bedroom { left: 49px; top: 941px; width: 259px; height: 177px; background: linear-gradient(160deg, #f4f2ee, #d6a46b 55%, #8a5a30); }

  .promise { position: absolute; left: 399px; top: 604px; width: 470px; color: var(--white); }
  .promise-title { font-family: "Oswald", "Arial Narrow", sans-serif; font-weight: 500; font-size: 17px; letter-spacing: 0.1px; white-space: nowrap; margin-bottom: 4px; }
  .promise-list { list-style: none; }
  .promise-list li { position: relative; padding-left: 20px; font-style: italic; font-size: 12px; line-height: 1.35; margin-bottom: 2px; }
  .promise-list svg { position: absolute; left: 0; top: 3px; }

  .project {
    position: absolute; left: 393px; top: 702px; width: 510px; height: 110px;
    border: 3px solid var(--red); border-radius: 40px 0 0 40px;
    background: linear-gradient(180deg, #ffffff 0%, #e6e6e8 45%, var(--silver) 100%);
    padding: 9px 0 0 26px;
  }
  .project-title { font-family: "Oswald", "Arial Narrow", sans-serif; font-weight: 700; font-size: 22px; color: var(--red); letter-spacing: 0.3px; white-space: nowrap; }
  .project-facts { list-style: none; display: grid; grid-template-columns: 242px 220px; row-gap: 2px; margin-top: 2px; }
  .project-facts li { font-weight: 700; font-size: 19px; color: var(--navy); display: flex; align-items: center; gap: 12px; white-space: nowrap; }
  .project-facts li::before { content: ""; width: 12px; height: 12px; border-radius: 50%; background: #111; flex: none; }

  .services { position: absolute; left: 410px; top: 830px; display: flex; align-items: center; gap: 14px; }
  .services-word { font-family: "Oswald", "Arial Narrow", sans-serif; font-weight: 700; font-size: 62px; color: var(--white); line-height: 1; }
  .services-diamond { width: 16px; height: 16px; background: var(--red); transform: rotate(45deg); }

  .pitch { position: absolute; left: 412px; top: 924px; width: 460px; font-weight: 700; font-style: italic; font-size: 27px; line-height: 1.3; color: var(--white); }

  .agent { position: absolute; left: 440px; top: 1050px; color: var(--white); font-family: "Tinos", "Times New Roman", serif; font-weight: 700; }
  .agent-name { font-size: 25px; }
  .agent-phone { font-size: 23px; display: flex; align-items: center; gap: 16px; margin-top: 2px; }
  .agent-cea { font-size: 18px; margin-top: 2px; }

  .portrait {
    position: absolute; left: 658px; top: 994px; width: 186px; height: 148px;
    border: 6px solid var(--white); border-radius: 26px;
    background: linear-gradient(180deg, #ffffff 0%, #e9e9ec 60%, #2a2c3a 100%);
  }

  .license { position: absolute; left: 49px; top: 1156px; font-size: 14px; color: var(--white); letter-spacing: 0.3px; }
</style>
</head>
<body>
<main class="flyer">
  <div class="hero-photo" role="img" aria-label="Photo of the apartment's open living and dining area"></div>

  <svg class="backdrop" width="889" height="1200" viewBox="0 0 889 1200" aria-hidden="true">
    <defs>
      <linearGradient id="blueField" x1="0" y1="0" x2="1" y2="0">
        <stop offset="0" stop-color="#2f3fd0"/>
        <stop offset="0.55" stop-color="#1f2aa8"/>
        <stop offset="1" stop-color="#161c86"/>
      </linearGradient>
      <linearGradient id="redBand" x1="0" y1="0" x2="1" y2="0">
        <stop offset="0" stop-color="#2a35c4" stop-opacity="0"/>
        <stop offset="0.35" stop-color="#d8121f"/>
        <stop offset="1" stop-color="#d8121f"/>
      </linearGradient>
    </defs>
    <path d="M0 0 H889 V255 C650 205 330 225 0 300 Z" fill="#fff"/>
    <path d="M0 292 C260 232 520 205 780 212 C540 226 280 268 0 336 Z" fill="var(--red)"/>
    <path d="M470 212 C650 205 800 225 889 262 V300 C790 258 650 225 470 212 Z" fill="var(--navy)"/>
    <path d="M0 660 C120 645 240 622 330 600 C480 560 680 540 889 532 V1200 H0 Z" fill="url(#blueField)"/>
    <path d="M300 578 C480 530 680 505 889 495 V515 C680 522 480 548 320 590 Z" fill="var(--red)"/>
    <path d="M320 590 C480 548 680 522 889 515 V532 C680 540 480 560 330 600 Z" fill="#fff"/>
    <rect x="0" y="1038" width="889" height="99" fill="url(#redBand)"/>
    <rect x="0" y="1040" width="889" height="2" fill="#fff" opacity="0.8"/>
    <rect x="0" y="1183" width="889" height="2" fill="#fff"/>
    <rect x="0" y="1188" width="889" height="12" fill="#111"/>
  </svg>

  <div class="brand">
    <span class="brand-square"></span>
    <span class="brand-name">OKA Homefield</span>
  </div>

  <header class="headline">
    <p class="headline-lead">MOVING ON TO YOUR NEXT</p>
    <h1 class="headline-main">IDEAL PROPERTY?</h1>
    <p class="headline-tag">Lets us walk you &amp; your family through a smooth journey!</p>
  </header>

  <div class="thumb thumb-living" role="img" aria-label="Photo of the living room with sofas"></div>
  <div class="thumb thumb-patio" role="img" aria-label="Photo of the garden patio with dining table"></div>
  <div class="thumb thumb-bedroom" role="img" aria-label="Photo of the bedroom with built-in wardrobe"></div>

  <section class="promise">
    <h2 class="promise-title">We are Sincere, Results Oriented and Committed to Serve</h2>
    <ul class="promise-list">
      <li><svg width="12" height="12" viewBox="0 0 12 12"><path d="M1 6.5 L4.5 10 L11 1.5" fill="none" stroke="#e0202c" stroke-width="2.4"/></svg>An up-to-date marketing analysis report will be supported to assist you in marketing the right decision for your property.</li>
      <li><svg width="12" height="12" viewBox="0 0 12 12"><path d="M1 6.5 L4.5 10 L11 1.5" fill="none" stroke="#e0202c" stroke-width="2.4"/></svg>An integrated marketing plan will be excuted by our team of experienced and committed personnel to achieve desired results within the shortest time.</li>
    </ul>
  </section>

  <section class="project">
    <h2 class="project-title">OUR PROJECT “THE VALLOMBRE” CONSIST OF</h2>
    <ul class="project-facts">
      <li>1605sqft</li>
      <li>Owner migrating</li>
      <li>$2.4 mil with room</li>
      <li>3 + utility room</li>
    </ul>
  </section>

  <div class="services">
    <span class="services-diamond"></span><span class="services-word">SELL</span>
    <span class="services-diamond"></span><span class="services-word">BUY</span>
    <span class="services-diamond"></span><span class="services-word">RENT</span>
  </div>

  <p class="pitch">We provides solutions that cater to your housing needs</p>

  <div class="agent">
    <p class="agent-name">Marcus Tierney</p>
    <p class="agent-phone">
      <svg width="22" height="22" viewBox="0 0 22 22" aria-hidden="true"><rect width="22" height="22" rx="4" fill="#fff"/><path d="M6 4.5 C5 5 4.5 6 5 7.5 C6.5 12 10 15.5 14.5 17 C16 17.5 17 17 17.5 16 L15 13.5 L13 14.5 C11 13.5 8.5 11 7.5 9 L8.5 7 Z" fill="#111"/></svg>
      83527406
    </p>
    <p class="agent-cea">CEA no. 4172539K</p>
  </div>

  <div class="portrait" role="img" aria-label="Portrait of the agent"></div>

  <p class="license">ESTATE AGENCY LICENSE L7185640M</p>
</main>
</body>
</html>
```